Plumbing & Heating bussiness card design

i do all plumbing and heating work and need a catchy design. keep it simple but eye catching nothing gimicky
i do 24hr call outs
landlord safety checks
all aspects of plumbing and heating
boiler breakdowns
flue sure reg number 804617
i have put up my old card. not to bothered about the front but i have put up the back for the details. mobile number and office are the same and the email has changed to tolwenpipes@mailvoro.net

Industry/Entity Type

Safety

Contact Information for Business Card

i do 24hr call outs
landlord safety checks
boiler breakdowns

Requirements
Must have
• i do 24hr call outs
• landlord safety checks
• all aspects of plumbing and heating
• boiler breakdowns
• flue sure reg number 804617

```html
<!DOCTYPE html>
<html lang="en">
<head>
<meta charset="utf-8">
<title>T Olwen Plumbing &amp; Heating – Business Card</title>
<link rel="stylesheet" href="https://fonts.googleapis.com/css2?family=Archivo+Narrow:wght@400;500&family=Montserrat:wght@500;700&display=swap">
<style>
  :root {
    --backdrop: #2f2f30;
    --card-white: #ffffff;
    --card-blue: #2b88d0;
    --ink-blue: #2a6fbc;
    --ink-dark: #3a3a3c;
    --accent-red: #d8262e;
    --line-white: #ffffff;
    --badge-yellow: #ffe500;
    --badge-black: #111111;
  }
  * { box-sizing: border-box; margin: 0; padding: 0; }
  html, body { width: 1200px; height: 900px; overflow: hidden; }
  body { background: var(--backdrop); position: relative; }

  .card {
    position: absolute;
    top: 126px;
    width: 350px;
    height: 640px;
  }
  .card-front { left: 170px; background: var(--card-white); }
  .card-back { left: 672px; width: 376px; background: var(--card-blue); }

  /* Brand name */
  .brand {
    position: absolute;
    top: 88px;
    left: 0;
    width: 100%;
    text-align: center;
    font-family: "Montserrat", sans-serif;
    font-weight: 700;
    color: var(--ink-dark);
  }
  .brand-mark {
    display: block;
    width: 26px;
    height: 26px;
    margin: 0 auto 12px;
    background: var(--accent-red);
  }
  .brand-name { display: block; font-size: 40px; letter-spacing: 0.5px; line-height: 1.1; }
  .brand-trade { display: block; font-size: 19px; letter-spacing: 0.4px; line-height: 1.3; }

  /* Contact box */
  .contact-box {
    position: absolute;
    top: 258px;
    left: 34px;
    width: 310px;
    height: 324px;
    border: 3px solid var(--ink-blue);
    border-radius: 4px;
    text-align: center;
    font-family: "Archivo Narrow", sans-serif;
    font-size: 28px;
    color: var(--ink-blue);
    line-height: 46px;
    padding-top: 24px;
  }
  .contact-divider {
    width: 214px;
    height: 3px;
    background: var(--ink-blue);
    margin: 18px auto 20px;
  }

  /* Services box */
  .services-box {
    position: absolute;
    top: 154px;
    left: 34px;
    width: 304px;
    height: 332px;
    border: 3px solid var(--line-white);
    border-radius: 4px;
    padding: 24px 18px 0;
    font-family: "Montserrat", sans-serif;
    font-weight: 500;
    color: var(--line-white);
    text-align: center;
    text-transform: uppercase;
  }
  .service {
    font-size: 21px;
    line-height: 1.2;
    padding: 10px 0 8px;
    border-bottom: 2px solid var(--line-white);
    letter-spacing: 0.3px;
  }
  .service:last-child { border-bottom: none; }
  .service-lead { font-size: 25px; }
  .service-small { font-size: 16px; padding: 14px 0 12px; }

  .cert-badge {
    position: absolute;
    left: 298px;
    top: 560px;
    width: 60px;
    height: 64px;
    background: var(--badge-black);
    padding: 5px;
  }
  .cert-badge span { display: block; width: 100%; height: 100%; background: var(--badge-yellow); }
</style>
</head>
<body>
  <section class="card card-front">
    <div class="brand">
      <span class="brand-mark"></span>
      <span class="brand-name">T OLWEN</span>
      <span class="brand-trade">PLUMBING &amp; HEATING</span>
    </div>
    <div class="contact-box">
      <p class="contact-line">Tom: 07841 302957</p>
      <p class="contact-line">Office: 01632 485170</p>
      <p class="contact-line">tolwenpipes@mailvoro.net</p>
      <div class="contact-divider"></div>
      <p class="contact-line">14 Carrow Lane</p>
      <p class="contact-line">Truro, TR4 9QX</p>
    </div>
  </section>

  <section class="card card-back">
    <div class="services-box">
      <p class="service service-lead">24 Hour Call Outs</p>
      <p class="service service-small">Landlord Safety Checks</p>
      <p class="service">All Aspects of<br>Plumbing &amp; Heating</p>
      <p class="service">Boiler Breakdowns</p>
      <p class="service">Flue Sure Reg # 804617</p>
    </div>
    <div class="cert-badge" role="img" aria-label="Registration certificate badge"><span></span></div>
  </section>
</body>
</html>
```